Banner Ads for Online Poker Promotion

We are an online poker network, the KLV (www.theklvnet.eu). We are looking for a small selection of web banner ads for our latest promotion.

Banner sizes that we need are:
- 196x523 (static .psd and .png)
- 199x129 (static .psd and .png)
- 447x426 (static .psd and .png)
- 500x400 (static .psd and .png)
- 697x167 (static .psd and .png)
- 460x60 (animated .gif)

The promotion name is ‘Rush & Deal Plunder’ (or ‘RND Plunder’) and the concept is that certain Sit & Go tournaments have money added to the prize pool. Basically, free cash for Sit & Go players.

(If you don’t know poker, a ‘Sit & Go’ is a tournament which starts when a specific number of players join, as opposed to a scheduled tournament which starts at a specific time).

The promotion starts on November 3rd.

Guidelines:

The name of the promotion, ‘Rush & Deal Plunder’ or ‘RND Plunder’, should feature prominently in the banners.

The strap line can be ‘Get Your Share of the Loot’, ‘Added Money in SNGs’ or something similar (feel free to be creative).

Our network logo (attached) must feature on the animated .gif. It is optional on the other banners.

Examples of past promotional imagery can be found on our website, in particular these pages: http://www.theklvnet.eu/promotions/ and http://www.theklvnet.eu/promotions/archived-promotions/ . Our last promotion was crowdsourced and the details of that and the winner can be found here: http://jobs.artquarry.com/job.aspx?id=512047

We are looking to go in a more modern and risqué direction than the past, in order to stand out from competition which is very bland.

Common poker imagery –cards, chips, suit icons etc – or objects associated with live poker (tables, etc) is a little clichéd. It can be included if it has a clear purpose. But don’t just put flying cards or suit symbols in there for no reason.

More like vexOS4/5, less like vexOS3

Think flat, modern, glamour, clean, fresh, bright, rock music, extreme sports, and the Loud Stone!

Most of our customers are 18-35, male, and we have a strong European focus.

As we are a gaming company, the banners must not encourage underage play, problem gambling, or associate gambling with sexual or social success.

If any further guidance is needed please don’t hesitate to ask!

```html
<!DOCTYPE html>
<html lang="en">
<head>
<meta charset="utf-8">
<title>RND Plunder – Promotion Banner</title>
<link rel="stylesheet" href="https://fonts.googleapis.com/css2?family=Graduate&family=Open+Sans:wght@600;700&display=swap">
<style>
  :root {
    --felt-dark: #2f8a22;
    --felt-mid: #3aa82a;
    --table-light: #46c21e;
    --table-deep: #2f9e14;
    --letter-white: #ffffff;
    --letter-mint: #e4f7df;
    --outline-green: #1f7a18;
    --outline-dark: #0f4a0c;
    --chip-pink: #c2387f;
    --chip-blue: #2f5fb8;
    --chip-red: #b8292f;
    --chip-slate: #3a3a42;
    --chip-teal: #2aa39a;
  }
  html, body {
    margin: 0;
    padding: 0;
    overflow: hidden;
    background: #1c5e14;
  }
  .banner {
    position: relative;
    width: 1200px;
    height: 960px;
    overflow: hidden;
    background: linear-gradient(180deg, var(--table-light) 0%, var(--table-deep) 100%);
    font-family: "Open Sans", Arial, sans-serif;
    color: var(--letter-white);
    text-align: center;
  }
  .banner h1, .banner p {
    margin: 0;
    padding: 0;
  }
  .felt-wall {
    position: absolute;
    left: 0; top: 0;
    width: 1200px; height: 230px;
    background: radial-gradient(ellipse at 50% 40%, var(--felt-mid) 0%, var(--felt-dark) 75%);
  }
  .table-surface {
    position: absolute;
    left: 0; top: 228px;
    width: 1200px; height: 732px;
  }
  .chip-stacks {
    position: absolute;
    top: 160px;
    width: 230px;
    height: 420px;
    border-radius: 30px;
    background: linear-gradient(180deg, var(--chip-pink) 0%, var(--chip-blue) 25%, var(--chip-red) 50%, var(--chip-slate) 72%, var(--chip-teal) 100%);
    opacity: 0.85;
  }
  .chip-stacks--left { left: -20px; }
  .chip-stacks--right { right: -20px; }
  .block-text {
    position: absolute;
    left: 0;
    width: 1200px;
    font-family: "Graduate", "Times New Roman", serif;
    font-weight: 400;
    -webkit-text-stroke: 6px var(--outline-green);
    paint-order: stroke fill;
    line-height: 1;
    transform-origin: 50% 0;
  }
  .promo-short {
    top: 65px;
    font-size: 250px;
    letter-spacing: 6px;
    color: var(--letter-white);
    transform: scaleY(1.25);
    text-shadow: 0 5px 0 var(--outline-dark), 0 8px 12px rgba(0,0,0,0.35);
  }
  .promo-long {
    position: absolute;
    left: 0; width: 1200px;
    top: 384px;
    font-size: 70px;
    font-weight: 600;
    line-height: 1;
    text-shadow: 0 3px 6px rgba(0,0,0,0.3);
  }
  .promo-word {
    top: 479px;
    font-size: 150px;
    letter-spacing: 4px;
    color: var(--letter-mint);
    transform: scaleY(1.1);
    text-shadow: 0 5px 0 var(--outline-dark), 0 8px 12px rgba(0,0,0,0.3);
  }
  .start-label {
    position: absolute;
    left: 0; width: 1200px;
    top: 662px;
    font-size: 38px;
    font-weight: 600;
    line-height: 1;
  }
  .start-date {
    position: absolute;
    left: 0; width: 1200px;
    top: 714px;
    font-size: 54px;
    font-weight: 600;
    line-height: 1;
    letter-spacing: 1px;
  }
  .network-name {
    position: absolute;
    left: 0; width: 1200px;
    top: 860px;
    font-size: 52px;
    font-weight: 600;
    line-height: 1;
    letter-spacing: 4px;
    color: var(--letter-mint);
  }
</style>
</head>
<body>
  <main class="banner">
    <div class="felt-wall"></div>
    <svg class="table-surface" viewBox="0 0 1200 732" width="1200" height="732" aria-hidden="true">
      <g fill="#ffffff" opacity="0.07">
        <polygon points="520,0 560,0 300,732 120,732"/>
        <polygon points="640,0 680,0 1080,732 900,732"/>
        <polygon points="585,0 615,0 660,732 540,732"/>
      </g>
      <rect x="0" y="0" width="1200" height="6" fill="#5fd43a" opacity="0.6"/>
    </svg>

    <div class="chip-stacks chip-stacks--left" role="img" aria-label="Stacks of pink, blue, red, black and teal poker chips"></div>
    <div class="chip-stacks chip-stacks--right" role="img" aria-label="Stacks of pink, blue, red, black and teal poker chips"></div>

    <h1 class="block-text promo-short">RND</h1>
    <p class="promo-long">Rush &amp; Deal</p>
    <p class="block-text promo-word">PLUNDER</p>
    <p class="start-label">Promotion Starts on</p>
    <p class="start-date">November 3rd</p>
    <p class="network-name">KLV</p>
  </main>
</body>
</html>
```